High End Notary Service Business Card Design

Want a professional and elegant/luxurious business card that is clean and simple in the design. A notary is a trusted professional that helps people sign very important documents. The card should be in alignment with this service provided.

Most of the time, service will be for the purchase of a home or refinance of a mortgage

There is NO LOGO. This is aesthetic. A look and feel. Conveying professionalism and concierge level of service.

Target Market(s)

Other business professionals, Lawyers, Escrow Officers, Loan Officers

Industry/Entity Type

Legal

Contact Information for Business Card

This will be a one-sided business card

Colors
35a7d7
3176b5
85cae6
d3a5cc
b868aa
ffffff
0356a4

Requirements
Must have
• Doreen L. Marsh-Whitlock
Notary Public

614-872-3916
MarshPublicNotary@Vornmail.com
Nice to have
• Headshot photo below. Convey the aspect of signing documents. No black cards. Preference is shades of blue: light blue, navy, aqua, gold, white, or lavendar, etc.
Should not have
• No scales or legal scales.

```html
<!DOCTYPE html>
<html lang="en">
<head>
<meta charset="utf-8">
<title>Doreen L. Marsh-Whitlock — Notary Public Business Card</title>
<link rel="stylesheet" href="https://fonts.googleapis.com/css2?family=Montserrat:ital,wght@0,400;0,500;0,600;1,400&display=swap">
<style>
  :root {
    --page-bg: #ffffff;
    --plum: #a55d9b;
    --orchid: #b868aa;
    --lavender: #d3a5cc;
    --band-grey: #efedef;
    --white: #ffffff;
    --label-ink: #231f20;
  }
  * { box-sizing: border-box; margin: 0; padding: 0; }
  html, body {
    width: 1200px;
    height: 1200px;
    overflow: hidden;
    background: var(--page-bg);
    font-family: "Montserrat", Arial, sans-serif;
  }
  .canvas {
    position: relative;
    width: 1200px;
    height: 1200px;
  }
  .size-label {
    position: absolute;
    left: 223px;
    top: 338px;
    font-size: 22px;
    font-weight: 400;
    color: var(--label-ink);
  }
  .card {
    position: absolute;
    left: 223px;
    top: 384px;
    width: 754px;
    height: 432px;
    background: var(--plum);
    overflow: hidden;
  }
  .signature-script {
    position: absolute;
    left: 52px;
    top: 102px;
    width: 648px;
    height: 131px;
    border-radius: 60px;
    background: linear-gradient(100deg, rgba(255,255,255,0.18), rgba(211,165,204,0.45) 50%, rgba(255,255,255,0.15));
  }
  .identity {
    position: absolute;
    right: 60px;
    top: 293px;
    text-align: right;
    color: var(--white);
  }
  .identity__name {
    font-size: 25px;
    font-weight: 400;
    line-height: 1.1;
  }
  .identity__title {
    margin-top: 8px;
    font-size: 17px;
    font-style: italic;
    font-weight: 400;
  }
  .contact-band {
    position: absolute;
    left: 0;
    top: 364px;
    width: 754px;
    height: 68px;
  }
  .contact-line {
    position: absolute;
    right: 60px;
    top: 380px;
    font-size: 16px;
    font-weight: 600;
    letter-spacing: 1px;
    color: var(--orchid);
    white-space: nowrap;
  }
  .contact-line .divider { margin: 0 12px; }
</style>
</head>
<body>
<main class="canvas">
  <p class="size-label">Size: 3.5” x 2”</p>

  <section class="card">
    <div class="signature-script" role="img" aria-label="Signature-style script lettering of the first name Doreen"></div>

    <div class="identity">
      <h1 class="identity__name">Doreen L. Marsh-Whitlock</h1>
      <p class="identity__title">Notary Public</p>
    </div>

    <svg class="contact-band" viewBox="0 0 754 68" aria-hidden="true">
      <rect x="0" y="0" width="754" height="50" fill="var(--white)"/>
      <rect x="110" y="4" width="644" height="44" fill="var(--band-grey)"/>
      <polygon points="96,0 120,0 140,24 120,48 96,48 116,24" fill="var(--orchid)"/>
      <rect x="0" y="50" width="754" height="18" fill="var(--orchid)"/>
    </svg>

    <p class="contact-line">
      <span class="contact-line__phone">614-872-3916</span><span class="divider">|</span><span class="contact-line__email">MarshPublicNotary@Vornmail.com</span>
    </p>
  </section>
</main>
</body>
</html>
```